Sharpen Your Calling book cover and updated company logo bundle

USE THE LOGO ON THE BACK COVER. I WANT AN UPDATED LOOK TO MY LOGO
Size of book: 5.5 x 8.5
Title: Sharpen Your Calling
Subtitle: An introvert’s guide to creating a coaching business that reflects who you are
The Subtitle does NOT go on the book cover
Author: Marla Trundell
BOOK DESCRIPTION: This book will help coaches and creative professionals get confidently clear on who they are so they can create a business that reflects their inner message.

DEMOGRAPHICS — Coaches and creative professional age 35-45

WOULD YOU PREFER PEOPLE OR OBJECTS ON YOUR COVER?
Objects or abstract designs
Anything I don’t want on the cover? people
Objects or symbols I want on the cover: possibly magnifying glass

IF YOU HAVE ANY PHOTOS THAT YOU WOULD LIKE US TO USE, PLEASE INCLUDE THE LINK(S) HERE. My logo or face pic for the back cover (Face pic pending)

COPY FOR THE SPINE
Sharpen Your Calling
Marla Trundell
Lantern Hill Press (with logo)

COPY FOR THE BACK COVER (270 words) my biz logo at the bottom and my picture next to my short bio. (Picture to come)

Create a Coaching Business that Reflects Who You Are

Do you want to step confidently into your new career by doing what you love? You aren't alone! But instead of doing what they love, many new coaches get stuck by trying to fit into traditional ways of doing business and create many unnecessary hurdles to happiness and success.
In this book, creative business coach, Marla Trundell teaches you, as she has taught herself and many others, to stop feeling guilty about what you “should” do in your life and in the process you will learn how to turn your passion into a purposeful career.

New coaches will learn how to:
• Recognize how your life decisions to this point are holding you back.
• Discover your gifts so you can express yourself through your creative projects.
• Identify and develop tools to bring your passion into purpose
• Offer services based on what you love to do.
• Understand your personal work style and work-flow to optimize your ideas and productivity.
• Create a message that reflects who you are to attract clients to work with you.
• Ask confidently for what you are worth and get it every time.
Join Marla on the journey of reconnecting with yourself and manifesting your dream.

Marla Trundell, founder of Harbor Heart and Soul, helps new coaches and creative entrepreneurs find their inner voice so that they have the confidence to bring their authentic selves out into the world. Marla has gone through this process for herself and helped other new businesses achieve dramatic improvements in their organization and focus as a result.

Target Market(s)

indicated in description

Industry/Entity Type

Life Coaching

Logo Text

Harbor Heart and Soul

Requirements
Must have
• updated look on existing logo it is going on the back of the book
Nice to have
• I like the font in the book cover I attached but Id like to see what else is possible

```html
<!DOCTYPE html>
<html lang="en">
<head>
<meta charset="utf-8">
<title>Sharpen Your Calling – Book Cover</title>
<link href="https://fonts.googleapis.com/css2?family=Ubuntu:ital,wght@0,300;0,400;1,300&display=swap" rel="stylesheet">
<style>
  :root {
    --ink: #1f1f1f;
    --body-grey: #6b6b6b;
    --title-grey: #7a7a7a;
    --orange: #f07a2a;
    --bullet: #f2b634;
    --spine-blue: #dce9f7;
    --paper: #ffffff;
    --glass-light: #e4edf6;
    --glass-handle: #f3c93a;
    --portrait: #111111;
  }
  * { margin: 0; padding: 0; box-sizing: border-box; }
  html, body { width: 1200px; height: 850px; overflow: hidden; background: var(--paper); }
  .cover {
    position: relative; width: 1200px; height: 850px;
    font-family: "Ubuntu", sans-serif; background: var(--paper);
  }

  /* Back cover */
  .back { position: absolute; left: 0; top: 0; width: 550px; height: 850px; }
  .back-heading {
    position: absolute; left: 47px; top: 62px;
    font-size: 16px; font-weight: 400; color: var(--ink); letter-spacing: 0.02em;
  }
  .back-copy {
    position: absolute; left: 47px; top: 90px; width: 490px;
    font-size: 10.2px; font-weight: 300; line-height: 24px; color: var(--body-grey);
  }
  .learn-heading {
    position: absolute; left: 47px; top: 279px;
    font-size: 15px; font-weight: 400; color: var(--ink);
  }
  .learn-list {
    position: absolute; left: 47px; top: 303px; width: 490px; list-style: none;
    font-size: 10.2px; font-weight: 300; line-height: 24px; color: var(--body-grey);
  }
  .learn-list li { padding-left: 12px; position: relative; }
  .learn-list li::before {
    content: "•"; position: absolute; left: 0; color: var(--bullet);
  }
  .learn-close {
    position: absolute; left: 47px; top: 471px;
    font-size: 10.2px; font-weight: 300; line-height: 24px; color: var(--body-grey);
  }
  .author-portrait {
    position: absolute; left: 47px; top: 544px; width: 165px; height: 170px;
    background: var(--portrait);
  }
  .author-bio {
    position: absolute; left: 239px; top: 543px; width: 285px;
    font-size: 10.2px; font-style: italic; font-weight: 300; line-height: 24px; color: var(--ink);
  }
  .client-mark {
    position: absolute; left: 52px; top: 778px; display: flex; align-items: center; gap: 8px;
    font-size: 15px; font-weight: 400; color: var(--orange);
  }
  .client-mark .dot { width: 22px; height: 22px; border-radius: 50%; background: var(--orange); }
  .publisher-back {
    position: absolute; left: 340px; top: 777px; display: flex; align-items: center; gap: 8px;
    font-size: 12px; font-weight: 300; color: var(--body-grey); letter-spacing: 0.04em;
  }
  .publisher-back .dot { width: 38px; height: 38px; border-radius: 50%; background: var(--ink); }

  /* Spine */
  .spine {
    position: absolute; left: 550px; top: 0; width: 100px; height: 850px;
    background: var(--spine-blue);
  }
  .spine-title {
    position: absolute; left: 26px; top: 16px; writing-mode: vertical-rl;
    font-size: 36px; font-weight: 300; letter-spacing: 0.04em; color: var(--title-grey);
    white-space: nowrap;
  }
  .spine-title .accent { color: var(--orange); }
  .spine-author {
    position: absolute; left: 33px; top: 448px; writing-mode: vertical-rl;
    font-size: 25px; font-weight: 300; letter-spacing: 0.28em; color: var(--title-grey);
    white-space: nowrap;
  }
  .spine-publisher {
    position: absolute; left: 0; top: 782px; width: 100px; text-align: center;
    font-size: 11px; font-weight: 300; color: var(--body-grey); line-height: 14px;
  }
  .spine-publisher .dot {
    display: block; width: 32px; height: 32px; border-radius: 50%; background: var(--ink);
    margin: 0 auto 8px;
  }

  /* Front cover */
  .front { position: absolute; left: 650px; top: 0; width: 550px; height: 850px; }
  .front-title {
    position: absolute; left: 0; top: 4px; width: 550px; text-align: center;
    font-weight: 300; line-height: 1;
  }
  .front-title .main {
    display: block; font-size: 84px; color: var(--title-grey); letter-spacing: 0.03em;
  }
  .front-title .accent {
    display: block; margin-top: 10px; font-size: 48px; color: var(--orange); letter-spacing: 0.04em;
  }
  .hero-object {
    position: absolute; left: 126px; top: 164px; width: 280px; height: 592px;
    border-radius: 140px 140px 40px 40px;
    background: linear-gradient(180deg, var(--glass-light) 0%, var(--glass-light) 55%, var(--glass-handle) 100%);
  }
  .front-author {
    position: absolute; left: 0; top: 794px; width: 550px; text-align: center;
    font-size: 34px; font-weight: 300; letter-spacing: 0.22em; color: var(--title-grey);
  }
</style>
</head>
<body>
<div class="cover">

  <section class="back">
    <h2 class="back-heading">Create a Coaching Business that Reflects Who You Are</h2>
    <p class="back-copy">Do you want to step confidently into your new career by doing what you love? You aren't alone! But instead of doing what they love, many new coaches get stuck by trying to fit into traditional ways of doing business and create many unnecessary hurdles to happiness and success.<br>In this book, creative business coach, Marla Trundell teaches you, as she has taught herself and many others, to stop feeling guilty about what you “should” do in your life and in the process you will learn how to turn your passion into a purposeful career.</p>

    <h3 class="learn-heading">New coaches will learn how to:</h3>
    <ul class="learn-list">
      <li>Recognize how your life decisions to this point are holding you back.</li>
      <li>Discover your gifts so you can express yourself through your creative projects.</li>
      <li>Identify and develop tools to bring your passion into purpose</li>
      <li>Offer services based on what you love to do.</li>
      <li>Understand your personal work style and work-flow to optimize your ideas and productivity.</li>
      <li>Create a message that reflects who you are to attract clients to work with you.</li>
      <li>Ask confidently for what you are worth and get it every time.</li>
    </ul>
    <p class="learn-close">Join Marla on the journey of reconnecting with yourself and manifesting your dream.</p>

    <div class="author-portrait" role="img" aria-label="Author portrait of Marla Trundell"></div>
    <p class="author-bio">Marla Trundell, founder of Harbor Heart and Soul, helps new coaches and creative entrepreneurs find their inner voice so that they have the confidence to bring their authentic selves out into the world. Marla has gone through this process for herself and helped other new businesses achieve dramatic improvements in their organization and focus as a result.</p>

    <div class="client-mark"><span class="dot"></span>Harbor Heart and Soul</div>
    <div class="publisher-back">Lantern Hill Press<span class="dot"></span></div>
  </section>

  <section class="spine">
    <div class="spine-title">Sharpen <span class="accent">Your Calling</span></div>
    <div class="spine-author">Marla Trundell</div>
    <div class="spine-publisher"><span class="dot"></span>Lantern Hill<br>Press</div>
  </section>

  <section class="front">
    <h1 class="front-title"><span class="main">Sharpen</span><span class="accent">Your Calling</span></h1>
    <div class="hero-object" role="img" aria-label="Illustration of a silver magnifying glass with a yellow handle"></div>
    <div class="front-author">Marla Trundell</div>
  </section>

</div>
</body>
</html>
```